UNIVERSITY OF CASTERBROOK SAXOPHONE SENIOR RECITAL

I need a poster design for my senior saxophone recital. The title of it is "Hollow: a Voyage across the Width of Tone". My concept is completely contrasting to the idea of a typical university recital. I'm so put off by the idea of "clap..clap..{play some music}..clap..clap..repeat". My recital is all based off of sound. The music I selected is all very modern (i.e Piet Halvermuss 'Warm Past the Final Pour' for Saxophone and Coffee Machine). I've included the Gatherly link so you can see the picture I have in the background. I like the idea of minimal black and white photography. Also, I would like the time / date / location / etc. all included on it. Let your imaginations run wild! It's art for an artist!
https://www.gatherly.example/events/413920587716230/
Target Market(s)
University Students around the University of Casterbrook and locals around the art district of South Beach, FL.
Industry/Entity Type
University

```html
<!DOCTYPE html>
<html lang="en">
<head>
<meta charset="UTF-8">
<title>Hollow: a Voyage across the Width of Tone — Senior Saxophone Recital</title>
<link rel="stylesheet" href="https://fonts.googleapis.com/css2?family=League+Gothic&family=Pathway+Gothic+One&family=Questrial&display=swap">
<style>
  :root {
    --page: #ffffff;
    --ink-black: #000000;
    --ink-white: #ffffff;
    --cloud-light: #c9c9c9;
    --cloud-mid: #8d8d8d;
    --mountain: #3a3a3a;
    --shadow: #050505;
    --brass-hi: rgba(190, 190, 190, 0.55);
  }
  html, body {
    margin: 0;
    width: 1200px;
    height: 900px;
    overflow: hidden;
    background: var(--page);
  }
  .poster {
    position: absolute;
    left: 321px;
    top: 30px;
    width: 550px;
    height: 844px;
    overflow: hidden;
    background: var(--shadow);
  }
  .poster__photo {
    position: absolute;
    inset: 0;
    background:
      radial-gradient(ellipse 120px 210px at 86% 78%, var(--brass-hi), transparent 75%),
      radial-gradient(ellipse 90px 330px at 91% 30%, rgba(160,160,160,0.35), transparent 80%),
      linear-gradient(to right, transparent 58%, rgba(10,10,10,0.75) 92%),
      linear-gradient(to bottom,
        var(--cloud-light) 0%,
        #b4b4b4 14%,
        var(--cloud-mid) 27%,
        var(--mountain) 38%,
        #2a2a2a 46%,
        #111111 53%,
        var(--shadow) 62%,
        var(--ink-black) 100%);
  }
  .poster__header {
    position: absolute;
    top: 38px;
    left: 0;
    right: 0;
    text-align: center;
    font-family: "League Gothic", "Arial Narrow", sans-serif;
    font-size: 31px;
    letter-spacing: 0.3px;
    line-height: 1;
    white-space: nowrap;
  }
  .poster__school { color: var(--ink-black); }
  .poster__event  { color: var(--ink-white); }
  .poster__divider { color: var(--ink-black); margin: 0 6px; }
  .poster__title {
    position: absolute;
    left: 52px;
    top: 236px;
    margin: 0;
    font-family: "League Gothic", "Arial Narrow", sans-serif;
    font-weight: 400;
    font-size: 222px;
    line-height: 1;
    color: var(--ink-white);
    letter-spacing: 1px;
  }
  .poster__subtitle {
    position: absolute;
    left: 54px;
    top: 433px;
    margin: 0;
    font-family: "Questrial", "Century Gothic", sans-serif;
    font-weight: 400;
    color: var(--ink-white);
    text-transform: uppercase;
  }
  .subtitle__line {
    display: block;
    font-size: 33px;
    line-height: 40px;
  }
  .subtitle__line--indent { padding-left: 64px; }
  .subtitle__line--large {
    font-size: 84px;
    line-height: 78px;
    margin-left: -5px;
  }
  .poster__details {
    position: absolute;
    left: 0;
    right: 0;
    top: 742px;
    text-align: center;
    font-family: "Pathway Gothic One", "Arial Narrow", sans-serif;
    font-size: 22px;
    line-height: 30px;
    color: var(--ink-white);
    letter-spacing: 0.4px;
  }
  .poster__details p { margin: 0; }
</style>
</head>
<body>
  <main class="poster">
    <div class="poster__photo" role="img" aria-label="Black and white photograph of a misty mountain lake under clouds, with a saxophonist's hands on a tenor saxophone at the right"></div>

    <header class="poster__header">
      <span class="poster__school">UNIVERSITY OF CASTERBROOK</span><span class="poster__divider">|</span><span class="poster__event">SENIOR SAXOPHONE RECITAL</span>
    </header>

    <h1 class="poster__title">HOLLOW:</h1>

    <h2 class="poster__subtitle">
      <span class="subtitle__line">A Voyage</span>
      <span class="subtitle__line">Across the</span>
      <span class="subtitle__line subtitle__line--indent">Width of</span>
      <span class="subtitle__line subtitle__line--large">Tone</span>
    </h2>

    <section class="poster__details">
      <p>Sunday &nbsp;|&nbsp; December 2 &nbsp;|&nbsp; 7:00 PM &nbsp;|&nbsp; 555.014.2290</p>
      <p>Larkfield Theater | Heron Drive | New Alder | NY 10999</p>
    </section>
  </main>
</body>
</html>
```